Halloway Crest Backers Guild business cards

Create a single-sided business card for the Halloway Crest Backers Guild based on the attached logo.
The additional data fields include Name, Title, Email, Phone, and website.
Please use the following as sample data:
Name: Dean Varrow
Title: Co-Founder / Investor
Email: deanvarrow@mailtern.net
Phone: 555-314-2706
Website: www.hcbackersguild.com

Target Market(s)

Start ups, entrepreneurs, venture capitalists

Industry/Entity Type

Investment

Contact Information for Business Card

Professional business card. Technology company.

Font styles to use
Serif
Sans Serif

Requirements
Must have
• Include the HCBG logo (attached)
• Name
• Title
• Email
• Phone
• Website
Should not have
• Cute, cartoony

```html
<!DOCTYPE html>
<html lang="en">
<head>
<meta charset="utf-8">
<title>Halloway Crest Backers Guild — Business Card</title>
<link href="https://fonts.googleapis.com/css2?family=Lato:wght@400;700&display=swap" rel="stylesheet">
<style>
  :root {
    --canvas: #e9e7e3;
    --card: #ffffff;
    --charcoal: #3d3b3a;
    --ink: #4a4a4a;
    --green: #169a45;
    --rule: #b9b9b9;
  }
  html, body {
    margin: 0;
    width: 1200px;
    height: 800px;
    overflow: hidden;
    background: var(--canvas);
    font-family: "Lato", Arial, sans-serif;
  }
  .card {
    position: absolute;
    left: 75px;
    top: 100px;
    width: 1050px;
    height: 600px;
    background: var(--card);
    border-radius: 22px;
    overflow: hidden;
    box-shadow: 0 10px 30px rgba(0,0,0,0.12);
  }
  .card-bands {
    position: absolute;
    inset: 0;
    width: 1050px;
    height: 600px;
  }
  .band-top { fill: var(--charcoal); }
  .band-bottom { fill: var(--green); }

  .brand {
    position: absolute;
    left: 105px;
    top: 252px;
    display: flex;
    align-items: center;
    gap: 22px;
  }
  .brand-mark {
    width: 46px;
    height: 46px;
    border-radius: 50%;
    background: var(--green);
    flex: none;
  }
  .brand-name {
    margin: 0;
    color: var(--green);
    font-weight: 400;
    font-size: 31px;
    line-height: 1.15;
  }

  .contact-block {
    position: absolute;
    left: 578px;
    top: 140px;
    width: 400px;
  }
  .person-name {
    margin: 0;
    color: var(--ink);
    font-size: 38px;
    font-weight: 400;
    letter-spacing: 0.5px;
    line-height: 1;
  }
  .person-name strong { font-weight: 700; }
  .person-title {
    margin: 8px 0 0;
    color: var(--green);
    font-size: 21px;
    font-weight: 700;
  }
  .divider {
    width: 378px;
    height: 2px;
    background: var(--rule);
    margin: 30px 0 28px;
    border: 0;
  }
  .contact-list {
    list-style: none;
    margin: 0;
    padding: 0;
  }
  .contact-item {
    display: flex;
    align-items: center;
    gap: 22px;
    color: var(--ink);
    font-size: 25px;
    height: 44px;
  }
  .contact-icon {
    width: 22px;
    height: 22px;
    fill: var(--green);
    flex: none;
  }
</style>
</head>
<body>
  <div class="card">
    <svg class="card-bands" viewBox="0 0 1050 600" aria-hidden="true">
      <path class="band-top" d="M505,0 C548,0 560,56 612,56 L1050,56 L1050,0 Z"/>
      <path class="band-bottom" d="M0,508 C45,500 62,546 112,548 L440,556 C488,558 505,600 548,600 L0,600 Z"/>
    </svg>

    <div class="brand">
      <span class="brand-mark"></span>
      <p class="brand-name">Halloway Crest<br>Backers Guild</p>
    </div>

    <div class="contact-block">
      <h1 class="person-name"><strong>DEAN</strong> VARROW</h1>
      <p class="person-title">Co-Founder / Investor</p>
      <hr class="divider">
      <ul class="contact-list">
        <li class="contact-item">
          <svg class="contact-icon" viewBox="0 0 24 24" aria-hidden="true"><path d="M6.6 10.8a15.1 15.1 0 0 0 6.6 6.6l2.2-2.2a1 1 0 0 1 1-.25 11.4 11.4 0 0 0 3.6.57 1 1 0 0 1 1 1V20a1 1 0 0 1-1 1A17 17 0 0 1 3 4a1 1 0 0 1 1-1h3.5a1 1 0 0 1 1 1c0 1.25.2 2.45.57 3.57a1 1 0 0 1-.25 1z"/></svg>
          <span>555-314-2706</span>
        </li>
        <li class="contact-item">
          <svg class="contact-icon" viewBox="0 0 24 24" aria-hidden="true"><path d="M2 5h20v14H2z M2 5l10 8 10-8" fill="var(--green)" stroke="#fff" stroke-width="1.6" stroke-linejoin="round"/></svg>
          <span>deanvarrow@mailtern.net</span>
        </li>
        <li class="contact-item">
          <svg class="contact-icon" viewBox="0 0 24 24" aria-hidden="true"><circle cx="12" cy="12" r="10"/><g fill="none" stroke="#fff" stroke-width="1.4"><ellipse cx="12" cy="12" rx="4.2" ry="10"/><path d="M2 12h20M4 7h16M4 17h16"/></g></svg>
          <span>www.hcbackersguild.com</span>
        </li>
      </ul>
    </div>
  </div>
</body>
</html>
```